wedding package brochure

We want to freshen the look for our wedding packages. Attached is a link to the current content
http://www.tarwinheadslinks.com.au/weddings/THL-Wedding-Package-2012-2013.pdf
We would like the logo (the dolphins) included and it needs to showcase the beachside location and give a classy wedding feel. I have a style guide available if required.

Industry/Entity Type

Wedding

```html
<!DOCTYPE html>
<html lang="en">
<head>
<meta charset="utf-8">
<title>Buffet Selection Menu One – Tarwin Heads Links</title>
<link href="https://fonts.googleapis.com/css2?family=Oswald:wght@500;600&family=Roboto+Condensed:wght@400&display=swap" rel="stylesheet">
<style>
  :root {
    --red: #d7191f;
    --panel: #3a3b3d;
    --white: #ffffff;
    --body: #4a4a4a;
    --ink: #2b2b2b;
    --frame: #6b6b6b;
    --tick: #9a9a9a;
  }
  * { margin: 0; padding: 0; box-sizing: border-box; }
  html, body { width: 1200px; height: 423px; overflow: hidden; background: var(--white); }
  .spread { position: relative; width: 1200px; height: 423px; overflow: hidden; font-family: "Roboto Condensed", "Arial Narrow", sans-serif; }

  .hero-photo {
    position: absolute; left: 0; top: 0; width: 388px; height: 423px;
    background: radial-gradient(ellipse at 40% 40%, #e58a62 0%, #c9603e 35%, #7a4a35 65%, #3d4a2a 100%);
  }
  .menu-panel {
    position: absolute; left: 388px; top: 0; width: 209px; height: 423px;
    background: var(--panel); padding: 66px 14px 0 8px; color: var(--white);
  }
  .tick-band {
    position: absolute; top: 16px; left: 140px; width: 900px; height: 8px;
    background: repeating-linear-gradient(90deg, var(--tick) 0 1px, transparent 1px 3px);
    opacity: .75;
  }
  .page-no { position: absolute; top: 10px; font-family: "Oswald", sans-serif; font-weight: 500; font-size: 15px; color: var(--ink); }
  .page-no.left { left: 34px; }
  .page-no.right { left: 1141px; }
  .brand { position: absolute; top: 14px; left: 1052px; font-family: "Oswald", sans-serif; font-weight: 600; font-size: 7px; color: var(--red); letter-spacing: .1px; }

  .panel-title { font-family: "Oswald", sans-serif; font-weight: 600; font-size: 14.5px; margin-bottom: 12px; letter-spacing: -.1px; }
  .panel-title .accent { color: var(--red); }
  .dish-list { list-style: none; }
  .dish-list li { font-size: 9.6px; line-height: 13px; margin-bottom: 3px; }

  .photo-frame {
    position: absolute; left: 626px; width: 160px; height: 147px;
    border: 4px solid var(--frame); border-radius: 12px; overflow: hidden;
  }
  .photo-frame.pasta { top: 50px; background: linear-gradient(180deg, #f4f4f2 0%, #e9e3d6 55%, #d9b98a 70%, #f2f1ee 100%); }
  .photo-frame.tart { top: 211px; background: radial-gradient(circle at 45% 60%, #b25a5a 0%, #9c6b57 35%, #6e4a3c 65%, #3c2c26 100%); }

  .menu-section { position: absolute; left: 805px; width: 300px; }
  .menu-section.chilled { top: 57px; }
  .menu-section.dessert { top: 218px; }
  .section-title { font-family: "Oswald", sans-serif; font-weight: 600; font-size: 15px; color: var(--red); margin-bottom: 5px; }
  .menu-section .dish-list li { color: var(--body); font-size: 9.6px; line-height: 13px; margin-bottom: 3px; }

  .package-note {
    position: absolute; top: 380px; left: 597px; width: 563px; text-align: center;
    font-family: "Oswald", sans-serif; font-weight: 600; font-size: 14px; color: var(--red);
  }
</style>
</head>
<body>
<div class="spread">
  <div class="hero-photo" role="img" aria-label="Seared salmon fillet with grilled vegetables and parsley"></div>

  <section class="menu-panel">
    <h1 class="panel-title"><span class="accent">Buffet</span> Selection Menu One</h1>
    <ul class="dish-list">
      <li>Hot selection</li>
      <li>Seared Atlantic Salmon Fillets w Tarragon &amp; Vine Leaves</li>
      <li>Pepper Crust Eye Fillet Medallions on Garlic Mash</li>
      <li>Whole Local King Prawns Grilled w Sweet Soy &amp; Ginger on Fried Noodles</li>
      <li>Rump Steak and Tomato Sausages</li>
      <li>Crispy Skin Chicken Pieces in Lime and Chilli</li>
      <li>Sweet Potato Lasagne w English Spinach, Roasted Capsicum and Ricotta</li>
      <li>Barbequed Fried Rice w Egg, Onion, Bacon and Mushroom</li>
      <li>Jacket Roasted Potatoes w Sour Cream and Chives</li>
    </ul>
  </section>

  <div class="tick-band"></div>
  <span class="page-no left">07</span>
  <span class="brand">TARWIN HEADS LINKS</span>
  <span class="page-no right">08</span>

  <div class="photo-frame pasta" role="img" aria-label="Plate of prawn spaghetti"></div>
  <section class="menu-section chilled">
    <h2 class="section-title">Chilled Selection</h2>
    <ul class="dish-list">
      <li>Australian Ocean King Prawns</li>
      <li>Clyde River Rock Oysters</li>
      <li>Atlantic Smoked Salmon</li>
      <li>Caesar Salad Bar</li>
      <li>Canadian Style Slaw</li>
      <li>Olive, Tomato, Feta and Spanish Onion Salad</li>
    </ul>
  </section>

  <div class="photo-frame tart" role="img" aria-label="Baked berry tarts"></div>
  <section class="menu-section dessert">
    <h2 class="section-title">Dessert Selection</h2>
    <ul class="dish-list">
      <li>Profiteroles Filled w Keeler's Cream on Dark Chocolate Ganache w Fresh Berries</li>
      <li>Mississippi Mud Slice w Sour Cherries &amp; Double Cream</li>
      <li>Baked Berry Cheese Cake</li>
      <li>Sliced Fresh Fruit Platter</li>
      <li>Australian Cheese Plate w Lavosch</li>
      <li>Accompaniments</li>
      <li>Baker's Basket of Fresh Rolls and Butter</li>
    </ul>
  </section>

  <p class="package-note">Includes Premium Beverage Package $102 per Person</p>
</div>
</body>
</html>
```